Business Card Design Project

I would like a business card created for a new company. This is a holding company that acts as my investment company. It holds real estate and service based companies. The name of the company is Lucernaria which is Italian for Lanternry. Defined as development or growth.
We currently have no logo. I really like some of the "different" cards out there. Potentially metallic or grey/black. That looks premium/hi-end and unique. I am not sure if your design would be specific to the card stock I end with our just logo/design/font.
Real Estate

```html
<!DOCTYPE html>
<html lang="en">
<head>
<meta charset="utf-8">
<title>Lucernaria Business Card</title>
<link href="https://fonts.googleapis.com/css2?family=Enriqueta:wght@400;700&display=swap" rel="stylesheet">
<style>
  :root {
    --backdrop: #d6d6d6;
    --card-dark: #404042;
    --card-light: #ffffff;
    --ink-dark: #3a3a3c;
    --ink-body: #4a4a4a;
    --brand-light: #d9d9d9;
    --tagline: #a9a9a9;
    --web: #c4c4c4;
    --edge-bar: #3a3a3c;
  }
  html, body {
    margin: 0;
    padding: 0;
    width: 1200px;
    height: 724px;
    overflow: hidden;
    background: var(--backdrop);
    font-family: "Enriqueta", Georgia, serif;
  }
  .canvas {
    position: relative;
    width: 1200px;
    height: 724px;
  }
  .card {
    position: absolute;
    top: 200px;
    width: 460px;
    height: 263px;
    overflow: hidden;
  }
  .card--front {
    left: 106px;
    background: var(--card-dark);
  }
  .card--back {
    left: 598px;
    width: 464px;
    background: var(--card-light);
  }
  .brand-name {
    position: absolute;
    left: 51px;
    top: 108px;
    margin: 0;
    font-size: 43px;
    font-weight: 700;
    line-height: 1;
    color: var(--brand-light);
  }
  .tagline {
    position: absolute;
    left: 52px;
    top: 154px;
    margin: 0;
    font-size: 19px;
    font-weight: 400;
    color: var(--tagline);
  }
  .website {
    position: absolute;
    left: 52px;
    top: 210px;
    margin: 0;
    font-size: 17px;
    font-weight: 700;
    color: var(--web);
  }
  .edge-bar {
    position: absolute;
    left: 0;
    top: 0;
    width: 5px;
    height: 100%;
    background: var(--edge-bar);
  }
  .contact {
    position: absolute;
    left: 26px;
    top: 94px;
    margin: 0;
    font-style: normal;
    color: var(--ink-body);
    font-size: 15px;
    line-height: 20px;
  }
  .contact__name {
    display: block;
    font-size: 18px;
    font-weight: 700;
    color: var(--ink-dark);
    margin-bottom: 1px;
  }
  .contact__line { display: block; }
  .brand-vertical {
    position: absolute;
    right: -4px;
    bottom: -2px;
    margin: 0;
    writing-mode: vertical-rl;
    transform: rotate(180deg);
    font-size: 44px;
    font-weight: 700;
    line-height: 1;
    color: var(--ink-dark);
  }
</style>
</head>
<body>
<main class="canvas">
  <section class="card card--front" aria-label="Card front">
    <h1 class="brand-name">Lucernaria</h1>
    <p class="tagline">real estate and services...</p>
    <p class="website">www.xxxx.com</p>
  </section>

  <section class="card card--back" aria-label="Card back">
    <div class="edge-bar"></div>
    <address class="contact">
      <span class="contact__name">Mr. Name Of Yours</span>
      <span class="contact__line">Designation</span>
      <span class="contact__line">Phone:</span>
      <span class="contact__line">Address Line1</span>
      <span class="contact__line">Address Line2</span>
      <span class="contact__line">Address Line3</span>
    </address>
    <p class="brand-vertical">Lucernaria</p>
  </section>
</main>
</body>
</html>
```